Postcard Design January 2015

I need a postcard designed to introduce my company to potential new customers in the UK. My company is TW Page Services based in Chester and we represent one of Poland's leading and long established book printers. We offer competitive pricing, consistently high levels of print and binding quality and industry leading levels of customer service. We have been meeting the print requirements of UK publishers for more than 10 years.
Updates

Industry/Entity Type

Industry

```html
<!DOCTYPE html>
<html lang="en">
<head>
<meta charset="utf-8">
<title>TW Page Services – Postcard</title>
<link rel="stylesheet" href="https://fonts.googleapis.com/css2?family=Old+Standard+TT:wght@400;700&family=Pinyon+Script&display=swap">
<style>
  :root {
    --backdrop: #b3b3b3;
    --leather-light: #b5773f;
    --leather-mid: #9a5f2c;
    --leather-dark: #6f3f18;
    --ink: #2b170b;
    --ink-soft: #4a2c18;
    --cream: #f4e4c9;
    --cream-light: #fbf4e8;
    --paper-white: #ffffff;
    --rule: #6b4a33;
  }
  * { margin: 0; padding: 0; box-sizing: border-box; }
  html, body { width: 1200px; height: 660px; overflow: hidden; }
  body {
    position: relative;
    background: var(--backdrop);
    font-family: "Old Standard TT", "Times New Roman", serif;
    color: var(--ink);
  }

  /* ---------- Front ---------- */
  .card-front {
    position: absolute;
    left: 41px; top: 60px;
    width: 545px; height: 422px;
    overflow: hidden;
    background: linear-gradient(180deg, var(--cream-light), var(--cream));
    box-shadow: 6px 8px 10px rgba(0,0,0,.45);
  }
  .card-front__art { position: absolute; inset: 0; width: 100%; height: 100%; }
  .brand-name {
    position: absolute;
    left: 0; right: 0; top: 96px;
    text-align: center;
    font-weight: 700;
    color: var(--ink);
    line-height: 1;
  }
  .brand-name__initials { display: block; font-size: 96px; letter-spacing: 4px; }
  .brand-name__words { display: block; font-size: 34px; letter-spacing: 0.5px; margin-top: 6px; }
  .tagline {
    position: absolute;
    left: 0; right: 0; top: 380px;
    text-align: center;
    color: var(--ink-soft);
  }
  .tagline__lead {
    position: absolute;
    left: 0; right: 0; top: -50px;
    text-align: center;
    font-family: "Pinyon Script", cursive;
    font-size: 44px;
    color: var(--ink-soft);
    line-height: 1;
  }
  .tagline__rest { font-size: 19px; font-weight: 700; letter-spacing: 0.5px; color: var(--ink); }

  /* ---------- Back ---------- */
  .card-back {
    position: absolute;
    left: 606px; top: 192px;
    width: 577px; height: 410px;
    background: linear-gradient(90deg, var(--cream) 0%, var(--cream-light) 55%, var(--paper-white) 100%);
    border: 1px solid #8a7560;
    box-shadow: 6px 8px 10px rgba(0,0,0,.45);
  }
  .message {
    position: absolute;
    left: 30px; top: 26px;
    width: 210px;
    font-size: 11.2px;
    line-height: 1.18;
    color: var(--ink-soft);
  }
  .message p { text-align: justify; margin-bottom: 12px; }
  .message__company { font-family: "Pinyon Script", cursive; font-size: 13px; }
  .message__benefits { list-style: none; margin-bottom: 14px; }
  .message__benefits li::before { content: "• "; }
  .message__phone { font-weight: 700; font-size: 12px; padding-left: 36px; color: var(--ink); }
  .divider {
    position: absolute;
    left: 261px; top: 31px;
    width: 2px; height: 308px;
    background: var(--rule);
  }
  .stamp-box {
    position: absolute;
    left: 443px; top: 25px;
    width: 59px; height: 76px;
    border: 3px solid var(--ink-soft);
    background: var(--paper-white);
    display: flex; align-items: center; justify-content: center;
    text-align: center;
    font-size: 10px; line-height: 1.15;
    color: var(--ink-soft);
  }
  .address-line {
    position: absolute;
    left: 289px; width: 216px;
    height: 1.5px;
    background: var(--rule);
  }
</style>
</head>
<body>

<section class="card-front" aria-label="Postcard front">
  <svg class="card-front__art" viewBox="0 0 545 422" preserveAspectRatio="none">
    <defs>
      <radialGradient id="leatherTone" cx="50%" cy="40%" r="70%">
        <stop offset="0%" stop-color="var(--leather-light)"/>
        <stop offset="65%" stop-color="var(--leather-mid)"/>
        <stop offset="100%" stop-color="var(--leather-dark)"/>
      </radialGradient>
    </defs>
    <polygon role="img" aria-label="Brown leather texture background" points="0,0 545,0 545,330 267,294 0,330" fill="url(#leatherTone)"/>
    <polyline points="0,336 267,300 545,336" fill="none" stroke="var(--ink)" stroke-width="3"/>
    <polyline points="0,346 267,310 545,346" fill="none" stroke="var(--ink)" stroke-width="2"/>
  </svg>

  <h1 class="brand-name">
    <span class="brand-name__initials">TW</span>
    <span class="brand-name__words">PAGE SERVICES</span>
  </h1>

  <p class="tagline">
    <span class="tagline__lead">Excellence</span>
    <span class="tagline__rest">IN BOOK PRINTING &amp; BINDING</span>
  </p>
</section>

<section class="card-back" aria-label="Postcard back">
  <div class="message">
    <p>At <span class="message__company">TW Page Services</span> we produce high quality paperback and hardback books in mono or full colour, with many binding options which include sewn, perfect, Wiro-o, and saddle stitched.</p>
    <p>We also offer professional print finishing like lamination, spot UV and foil stamping.</p>
    <p>With our strict quality control procedures, state-of-the-art production equipment, and top quality materials you can be sure that your book will look beautiful, feel great, and last for many years to come.</p>
    <ul class="message__benefits">
      <li>High quality book printing &amp; binding</li>
      <li>Competitive pricing</li>
      <li>Excellent customer service</li>
      <li>Weekly shipments in to the UK</li>
    </ul>
    <div class="message__phone">Tel: 01632 960418</div>
  </div>

  <div class="divider"></div>

  <div class="stamp-box">PLACE<br>STAMP<br>HERE</div>

  <div class="address-line" style="top:170px"></div>
  <div class="address-line" style="top:208px"></div>
  <div class="address-line" style="top:246px"></div>
  <div class="address-line" style="top:283px"></div>
  <div class="address-line" style="top:321px"></div>
</section>

</body>
</html>
```